I am a general contractor in Portland, Or. I would like a clean and simple design layout, maybe using the "didot" font, blue and dark bronze in colors are preferred. On one side of the card, it would be nice to have a logo(attached photo) and business name(OTK Construction). I don't need my job title on the card, just some thing along the lines of "oliver kemp, general contractor". Thanks much.

Target Market(s)

Adults from 30-55 years old. Middle to upper class.

Industry/Entity Type

Contractor

Contact Information for Business Card

OTK Construction
Oliver T. Kemp
2843 NE 71st Ave.
Portland, Or. 97348
503.962.7084

Font styles to use
Other font styles liked:
• didot

Colors
3277b5
7f7f7f

Requirements
Should not have
• Too much going on.

```html
<!DOCTYPE html>
<html lang="en">
<head>
<meta charset="utf-8">
<title>OTK Construction – Business Card</title>
<link rel="stylesheet" href="https://fonts.googleapis.com/css2?family=Jost:wght@700&family=Exo+2:wght@400;500&display=swap">
<style>
  :root {
    --page: #e9e9ec;
    --navy: #27307a;
    --royal: #3a55b0;
    --brand-blue: #2d3d91;
    --paper: #ffffff;
    --paper-shade: #e4e4e6;
    --silver: #b9bcc2;
    --ink-light: #ffffff;
  }
  * { box-sizing: border-box; margin: 0; padding: 0; }
  html, body { width: 1200px; height: 828px; overflow: hidden; background: var(--page); }
  .canvas { position: relative; width: 1200px; height: 828px; }

  .card {
    position: absolute;
    width: 540px; height: 309px;
    top: 260px;
    overflow: hidden;
    border-radius: 3px;
    box-shadow: 0 6px 18px rgba(0,0,0,.18);
    background: var(--paper);
  }
  .card--front { left: 40px; }
  .card--back  { left: 620px; }
  .card__art { position: absolute; inset: 0; width: 100%; height: 100%; }

  /* front */
  .brand {
    position: absolute; left: 110px; top: 38px;
    display: flex; align-items: center; gap: 12px;
  }
  .brand__dot { width: 34px; height: 34px; border-radius: 50%; background: var(--royal); flex: none; }
  .brand__name {
    font-family: "Jost", sans-serif; font-weight: 700;
    font-size: 32px; line-height: 1.02; color: var(--brand-blue);
  }
  .brand__name span { display: block; }
  .front__web {
    position: absolute; right: 40px; bottom: 34px;
    font-family: "Exo 2", sans-serif; font-size: 15px;
    letter-spacing: 5px; color: var(--ink-light);
  }

  /* back */
  .back__mark {
    position: absolute; left: 90px; top: 190px;
    font-family: "Jost", sans-serif; font-weight: 700;
    font-size: 46px; color: var(--brand-blue);
  }
  .contact {
    position: absolute; right: 26px; top: 26px;
    text-align: right; color: var(--ink-light);
    font-family: "Exo 2", sans-serif;
  }
  .contact__name { font-size: 20px; font-weight: 500; letter-spacing: 1.5px; }
  .contact__role { font-size: 12px; margin-top: 2px; }
  .contact__address { font-size: 12px; line-height: 1.4; margin-top: 26px; }
  .contact__list { list-style: none; margin-top: 18px; font-size: 11.5px; line-height: 1.6; }
  .contact__list li { display: flex; justify-content: flex-end; align-items: center; gap: 7px; }
  .contact__list svg { width: 11px; height: 11px; fill: none; stroke: var(--ink-light); stroke-width: 1.6; }
</style>
</head>
<body>
<main class="canvas">

  <section class="card card--front" aria-label="Business card front">
    <svg class="card__art" viewBox="0 0 540 309" preserveAspectRatio="none" aria-hidden="true">
      <defs>
        <linearGradient id="frontBand" x1="0" y1="1" x2="1" y2="0">
          <stop offset="0" stop-color="#27307a"/>
          <stop offset="1" stop-color="#3a55b0"/>
        </linearGradient>
      </defs>
      <path d="M0 222 C160 212 390 170 540 42 L540 309 L0 309 Z" fill="#b9bcc2"/>
      <path d="M0 232 C165 222 395 182 540 56 L540 309 L0 309 Z" fill="url(#frontBand)"/>
    </svg>
    <div class="brand">
      <span class="brand__dot"></span>
      <p class="brand__name"><span>OTK</span><span>Construction</span></p>
    </div>
    <p class="front__web">www.otkbuilds.com</p>
  </section>

  <section class="card card--back" aria-label="Business card back">
    <svg class="card__art" viewBox="0 0 540 309" preserveAspectRatio="none" aria-hidden="true">
      <defs>
        <linearGradient id="backField" x1="0" y1="1" x2="1" y2="0">
          <stop offset="0" stop-color="#27307a"/>
          <stop offset="1" stop-color="#3a55b0"/>
        </linearGradient>
        <radialGradient id="backPaper" cx=".35" cy=".6" r=".7">
          <stop offset="0" stop-color="#ffffff"/>
          <stop offset="1" stop-color="#e4e4e6"/>
        </radialGradient>
      </defs>
      <rect width="540" height="309" fill="url(#backField)"/>
      <path d="M0 96 C200 84 350 170 378 309 L0 309 Z" fill="#b9bcc2"/>
      <path d="M0 106 C192 96 338 176 366 309 L0 309 Z" fill="url(#backPaper)"/>
    </svg>
    <p class="back__mark">OTK</p>
    <div class="contact">
      <p class="contact__name">OLIVER KEMP</p>
      <p class="contact__role">General Contractor</p>
      <p class="contact__address">2843 NE 71st Ave.<br>Portland, Or. 97348</p>
      <ul class="contact__list">
        <li>503 962 7084
          <svg viewBox="0 0 12 12"><path d="M3 1 L5 3.5 L4 5 Q5.5 7 7 8 L8.5 7 L11 9 L9.5 11 Q4 10 1 2.5 Z"/></svg></li>
        <li>503 962 7085
          <svg viewBox="0 0 12 12"><rect x="3" y="1" width="6" height="10" rx="1"/></svg></li>
        <li>503 962 7086
          <svg viewBox="0 0 12 12"><rect x="1.5" y="4" width="9" height="6"/><path d="M3.5 4 V1.5 H8.5 V4"/></svg></li>
        <li>hello@otkbuilds.com
          <svg viewBox="0 0 12 12"><rect x="1" y="2.5" width="10" height="7"/><path d="M1 2.5 L6 6.5 L11 2.5"/></svg></li>
        <li>www.otkbuilds.com
          <svg viewBox="0 0 12 12"><circle cx="6" cy="6" r="5"/><path d="M1 6 H11 M6 1 Q3 6 6 11 Q9 6 6 1"/></svg></li>
      </ul>
    </div>
  </section>

</main>
</body>
</html>
```